Batch #27 - MEN'S NATURAL THERAPEUTIC INTIMATE WASH

Men's Natural Therapeutic INTIMATE Wash
BATCH #27

Design a 4 oz. stand up tube with flip top cap...
To be packaged in a carton/box

Formula contains Tea Tree OIL
Aloe Vera Gel
Coconut Oil

PRODUCT IS A WASH/SOAP

Helps with
- Jock Itch (tinea cruris)
- Skin Rashes
- Candida
- Itchy Skin

COLORS ON TUBE: Gray, Black, Lime Electric Green and Blue

PRODUCT FOR MEN!

Target Market(s)

MEN

Industry/Entity Type

Retail

Font styles to use
Sans Serif

Colors
9bcb3b
abd036
33a6d7
000000
c9c9c9

Requirements
Must have
• Colors... black, gray, electric green and blue
Nice to have
• Needs to look masculine appeal to the male consumer

```html
<!DOCTYPE html>
<html lang="en">
<head>
<meta charset="utf-8">
<title>Batch #27 Intimate Wash – Tube Labels</title>
<link rel="stylesheet" href="https://fonts.googleapis.com/css2?family=Questrial&family=Oswald:wght@300;400;500&display=swap">
<style>
  :root {
    --bg: #f4f9fc;
    --tube-black: #1c1c1c;
    --band-gray: #d9d9d9;
    --band-gray-edge: #c9c9c9;
    --lime: #d8ec1c;
    --lime-deep: #abd036;
    --lime-soft: #9bcb3b;
    --panel-green: #a9d83a;
    --cap: #2a2a2a;
    --cap-dark: #151515;
    --white: #ffffff;
    --ink: #111111;
  }
  * { box-sizing: border-box; margin: 0; padding: 0; }
  html, body { width: 1200px; height: 938px; overflow: hidden; background: var(--bg); }
  .stage { position: relative; width: 1200px; height: 938px; }

  .tube { position: absolute; display: flex; flex-direction: column; align-items: center; }
  .tube__body { width: 100%; display: flex; flex-direction: column; }
  .tube__crimp { background: var(--tube-black); }
  .tube__top { background: var(--tube-black); color: var(--white); text-align: right; }
  .tube__band { background: var(--band-gray); border-top: 3px solid var(--band-gray-edge); border-bottom: 3px solid var(--band-gray-edge); color: var(--ink); }
  .tube__green { background: linear-gradient(180deg, var(--lime) 0%, var(--lime-deep) 100%); position: relative; display: flex; flex-direction: column; align-items: center; }
  .tube__cap { background: linear-gradient(180deg, var(--cap) 0%, var(--cap-dark) 100%); border-radius: 0 0 14px 14px; position: relative; }
  .tube__cap::after { content: ""; position: absolute; left: 50%; bottom: 0; transform: translateX(-50%); width: 38%; height: 46%; border-radius: 40px 40px 0 0; background: #0d0d0d; }

  .ingredients { background: var(--panel-green); text-align: center; font-family: "Oswald", sans-serif; color: var(--ink); text-transform: uppercase; }
  .ingredients__head { display: block; font-size: 5px; letter-spacing: .3px; font-weight: 400; }
  .ingredients__item { display: block; font-weight: 500; }
  .ingredient-art { background: linear-gradient(160deg, #cfe63a 0%, #8a6a45 55%, #f2f2ee 80%, #9fd04a 100%); border-radius: 8px; opacity: .85; }
  .net { font-family: "Oswald", sans-serif; font-size: 13px; color: var(--ink); }

  /* small tube */
  .tube--small { left: 324px; top: 268px; width: 286px; }
  .tube--small .tube__crimp { height: 22px; }
  .tube--small .tube__top { height: 162px; font-family: "Questrial", sans-serif; padding: 34px 22px 0 0; }
  .tube--small .brand__word { display: block; font-size: 40px; letter-spacing: 3px; line-height: 1; }
  .tube--small .brand__num { display: block; font-size: 38px; line-height: 1; }
  .tube--small .tube__band { height: 66px; font-family: "Questrial", sans-serif; padding: 8px 0 0 20px; }
  .tube--small .band__sub { font-size: 14px; letter-spacing: .5px; display: block; }
  .tube--small .band__main { font-size: 27px; letter-spacing: 1.5px; display: block; line-height: 1.1; }
  .tube--small .tube__green { height: 196px; padding-top: 6px; }
  .tube--small .ingredients { width: 100px; padding: 3px 0 4px; }
  .tube--small .ingredients__item { font-size: 9.5px; letter-spacing: .6px; line-height: 1.2; }
  .tube--small .ingredient-art { width: 210px; height: 70px; margin-top: 30px; }
  .tube--small .net { margin-top: 10px; }
  .tube--small .tube__cap { width: 232px; height: 96px; }

  /* tall tube */
  .tube--tall { left: 651px; top: 96px; width: 237px; }
  .tube--tall .tube__crimp { height: 18px; }
  .tube--tall .tube__top { height: 242px; font-family: "Oswald", sans-serif; font-weight: 300; padding: 40px 14px 0 0; }
  .tube--tall .brand__word { display: block; font-size: 52px; line-height: 1; letter-spacing: 1px; }
  .tube--tall .brand__num { display: block; font-size: 44px; line-height: 1.05; }
  .tube--tall .tube__band { height: 96px; font-family: "Oswald", sans-serif; font-weight: 300; padding: 12px 0 0 14px; }
  .tube--tall .band__sub { font-size: 17px; display: block; }
  .tube--tall .band__main { font-size: 35px; display: block; line-height: 1.2; }
  .tube--tall .tube__green { height: 284px; padding-top: 10px; }
  .tube--tall .ingredients { width: 84px; padding: 3px 0 6px; }
  .tube--tall .ingredients__item { font-size: 11px; font-weight: 400; line-height: 1.55; }
  .tube--tall .ingredient-art { width: 178px; height: 130px; margin-top: 22px; }
  .tube--tall .tube__cap { width: 188px; height: 96px; }
</style>
</head>
<body>
<main class="stage">

  <section class="tube tube--small" aria-label="4 oz tube label">
    <div class="tube__body">
      <div class="tube__crimp"></div>
      <header class="tube__top">
        <span class="brand__word">BATCH</span>
        <span class="brand__num">#27</span>
      </header>
      <div class="tube__band">
        <span class="band__sub">Men's Natural Therapeutic</span>
        <span class="band__main">INTIMATE WASH</span>
      </div>
      <div class="tube__green">
        <div class="ingredients">
          <span class="ingredients__head">Formula contains</span>
          <span class="ingredients__item">Tea Tree Oil</span>
          <span class="ingredients__item">Aloe Vera Gel</span>
          <span class="ingredients__item">Coconut Oil</span>
        </div>
        <div class="ingredient-art" role="img" aria-label="Splashing coconut halves, aloe vera slices and green leaves"></div>
        <span class="net">4 oz</span>
      </div>
    </div>
    <div class="tube__cap" aria-hidden="true"></div>
  </section>

  <section class="tube tube--tall" aria-label="Tall tube label">
    <div class="tube__body">
      <div class="tube__crimp"></div>
      <header class="tube__top">
        <span class="brand__word">BATCH</span>
        <span class="brand__num">#27</span>
      </header>
      <div class="tube__band">
        <span class="band__sub">Men's Natural Therapeutic</span>
        <span class="band__main">INTIMATE WASH</span>
      </div>
      <div class="tube__green">
        <div class="ingredients">
          <span class="ingredients__head">Formula contains</span>
          <span class="ingredients__item">Tea Tree Oil</span>
          <span class="ingredients__item">Aloe Vera Gel</span>
          <span class="ingredients__item">Coconut Oil</span>
        </div>
        <div class="ingredient-art" role="img" aria-label="Splashing coconut halves, aloe vera slices and green leaves"></div>
      </div>
    </div>
    <div class="tube__cap" aria-hidden="true"></div>
  </section>

</main>
</body>
</html>
```